Awesome Podcast Artwork Needed :-)

I need an AWESOME piece of podcast artwork for a new podcast called "Brick By Brick Basics" :-)
The Podcast teaches "new" property investors... or people just starting out... the basics of property investing (real estate) by sharing tips, tricks, strategies, interviews etc.
I have a logo that I'm kind of happy with and have attached examples of it here labelled "Examples Of Logo". It basically consists of four houses hanging on some thread and although I'm certainly not saying you must use it. If you do want to use it, I would be open to you "modernising" it a bit - if needed - or rearranging the house images in a line (horizontally or vertically) or in a square... or indeed in anyway you feel works
In terms of design, I confess I'm really not sure what I want - only I certainly do want to give a sense my Podcast is about "Property Investing".
I have included 2 examples of artwork that my competition uses labelled "Competition Artwork 1&2". I have also included "My Attempt" at doing this... which I know isn't very good - because you can't clearly see the words and to be honest - it looks weak next to other podcast artwork (for example the "Beyond Rental Yields" artwork that I have included here). I have attached a mock up of a "Simulated Podvana Screen" so you can see what I mean when I say my example looks weak compared to the others.
Lastly here's my new website (it's not yet out there) but that may give you some ideas of what I like: https://brickbybrickbasics.com/home/
I'm excited to see what you come up with :-)
PS. The artwork needs to be 3000x3000 pixels with a DPI of 72
Target Market(s)
New property investors - people who want to learn how to invest in property (real estate)
Requirements
Must have
- The name "Brick By Brick Basics"
Nice to have
- If my logo... or a variation on my logo can be incorporated - that would be good - but not essential. I've attached examples but will happily consider modifications.
- Please do not feel however that you must include the logo.

```html
<!DOCTYPE html>
<html lang="en">
<head>
<meta charset="utf-8">
<title>Brick By Brick Basics – Podcast Artwork</title>
<link href="https://fonts.googleapis.com/css2?family=Anton&family=Open+Sans:ital,wght@0,600;0,800;1,700&display=swap" rel="stylesheet">
<style>
  :root {
    --navy: #262a3b;
    --navy-mid: #4a4e5e;
    --fog: #b9bcc4;
    --paper: #ffffff;
    --amber: #eca22a;
    --white-type: #f6f6f6;
    --mark-grey: #8a8e9a;
    --brand-ink: #262a3b;
    --photo-top: #9aa3b4;
    --photo-mid: #6f7c96;
    --photo-bottom: #2b3652;
  }
  html, body {
    margin: 0;
    padding: 0;
    overflow: hidden;
    background: var(--paper);
  }
  .artwork {
    position: relative;
    width: 1200px;
    height: 1200px;
    overflow: hidden;
    background: linear-gradient(180deg, var(--navy) 0%, var(--navy) 46%, var(--navy-mid) 62%, var(--fog) 80%, var(--paper) 100%);
  }
  .title {
    position: absolute;
    left: 0;
    top: 0;
    width: 1200px;
    height: 520px;
  }
  .title text {
    font-family: "Anton", "Oswald", sans-serif;
    font-size: 238px;
  }
  .title .accent { fill: var(--amber); }
  .title .light { fill: var(--white-type); }
  .podcast-icon {
    position: absolute;
    left: 1052px;
    top: 30px;
    width: 116px;
    height: 222px;
  }
  .host-credit {
    position: absolute;
    left: 600px;
    top: 505px;
    width: 560px;
    height: 200px;
  }
  .host-credit .with {
    font-family: "Open Sans", sans-serif;
    font-weight: 600;
    font-size: 44px;
    fill: var(--paper);
  }
  .host-credit .host-name {
    font-family: "Open Sans", sans-serif;
    font-weight: 700;
    font-style: italic;
    font-size: 118px;
    fill: var(--paper);
  }
  .brand-mark {
    position: absolute;
    left: 48px;
    top: 860px;
    display: flex;
    align-items: flex-start;
    gap: 24px;
  }
  .brand-mark .square {
    flex: none;
    width: 64px;
    height: 64px;
    margin-top: 14px;
    background: var(--amber);
  }
  .brand-mark .brand-name {
    font-family: "Open Sans", sans-serif;
    font-weight: 800;
    font-size: 76px;
    line-height: 88px;
    letter-spacing: -1px;
    color: var(--brand-ink);
  }
  .host-photo {
    position: absolute;
    left: 690px;
    top: 690px;
    width: 510px;
    height: 510px;
    border-radius: 220px 0 0 0;
    background: radial-gradient(ellipse at 55% 35%, var(--photo-top) 0%, var(--photo-mid) 45%, var(--photo-bottom) 100%);
  }
</style>
</head>
<body>
  <main class="artwork">
    <svg class="title" viewBox="0 0 1200 520" aria-label="Brick By Brick Basics">
      <text class="accent" x="44" y="252" textLength="560" lengthAdjust="spacingAndGlyphs">BRICK</text>
      <text class="light" x="626" y="252" textLength="380" lengthAdjust="spacingAndGlyphs">BY</text>
      <text class="accent" x="44" y="490" textLength="1120" lengthAdjust="spacingAndGlyphs">BRICK BASICS</text>
    </svg>

    <svg class="podcast-icon" viewBox="0 0 116 222" aria-label="Podcast microphone icon">
      <rect x="22" y="6" width="72" height="20" rx="4" fill="var(--paper)"/>
      <text x="58" y="21" text-anchor="middle" font-family="Open Sans, sans-serif" font-weight="800" font-size="12" fill="var(--navy)">PODCAST</text>
      <rect x="24" y="30" width="68" height="112" rx="34" fill="var(--paper)"/>
      <rect x="34" y="44" width="48" height="84" rx="24" fill="var(--mark-grey)"/>
      <path d="M8 112 v10 a50 50 0 0 0 100 0 v-10" fill="none" stroke="var(--paper)" stroke-width="10"/>
      <rect x="52" y="170" width="12" height="34" fill="var(--paper)"/>
      <rect x="10" y="198" width="96" height="22" rx="4" fill="var(--paper)"/>
    </svg>

    <svg class="host-credit" viewBox="0 0 560 200" aria-label="with Dan Mercer">
      <text class="with" x="148" y="52">with</text>
      <text class="host-name" x="10" y="152" textLength="530" lengthAdjust="spacingAndGlyphs">Dan Mercer</text>
    </svg>

    <div class="brand-mark">
      <span class="square"></span>
      <span class="brand-name">Brick By<br>Brick<br>Basics</span>
    </div>

    <div class="host-photo" role="img" aria-label="Portrait photo of the host, smiling, in a navy blazer and light blue shirt"></div>
  </main>
</body>
</html>
```